New Organic Skin Care Line Needs to Design a Product Label

***THE WINNER OF THIS PROJECT WILL MOST LIKELY BECOME THE EXCLUSIVE DESIGNER FOR OUR OTHER PRODUCT LABELS***

We need a label design for a new organic skin care product line called "Maple Fern Gala." This specific product is a 100% pure organic coconut oil. It's used for skin hydration, protection, and makeup removal.

Info to include on front label:

1. Logo: Maple Fern Gala (attached)
2. Product Name: Pure Coconut Oil (emphasize "organic" somewhere)
3. Slogan: Hydrate your skin and hair.
4. Size: 8 FL OZ 236mL

Attached is:

1. The brand logo "Maple Fern Gala" with a white background.
2. An image of the bottle we will use.
3. An image of the bottle with lines to show the size and placement of the label.
4. The brand logo "Maple Fern Gala" with a black background. (photoshop file)

What we need:

A simple mock up of the front side of the label on the bottle. We first want to know what it will look like on the bottle given the size and dimensions.

- We would like one label with a white background (including the logo with a white background).
- We would like a second label with a black background (including the logo with a black background, just need to make the black font white instead of black).

We can get a great idea of what to expect from the front side of the label so we will complete the back side once we identify a winner.
Updates

Apologies, but we are now using a different bottle. The previous one is now discontinued. Please view the two most recent images uploaded. One is an image of the new bottle by itself. The other is an image of that bottle with instructions. Please use your most recent designs on the new bottle. Feel free to make any modifications you see fit to compliment the new bottle shape. Added Friday, March 18, 2016

Reason: We are still working with the label company to finalize the size. Once the size is confirmed we will have to tweak labels based on finalized measurements.

Target Market(s)

Women, 18-70

Industry/Entity Type

Skin Care Product

Font styles to use
Decorative
Script

Requirements
Must have
• -"shabby sheek" and "cute" theme
• -soft organic feel
• -the ingredients are organic, pure, and natural. That should be an essence of the label.

```html
<!DOCTYPE html>
<html lang="en">
<head>
<meta charset="utf-8">
<title>Maple Fern Gala – Pure Coconut Oil Labels</title>
<link href="https://fonts.googleapis.com/css2?family=Cinzel:wght@400;500&display=swap" rel="stylesheet">
<style>
  :root {
    --canvas: #ffffff;
    --label-light: #ffffff;
    --label-dark: #000000;
    --ink-dark: #1a1a1a;
    --ink-light: #ffffff;
    --leaf-green: #9bc93d;
    --leaf-green-soft: #b7d96e;
    --blossom-pink: #e0287a;
    --soft-shadow: rgba(0, 0, 0, 0.08);
  }
  * { margin: 0; padding: 0; box-sizing: border-box; }
  html, body {
    width: 1200px;
    height: 1200px;
    overflow: hidden;
    background: var(--canvas);
  }
  .canvas {
    position: relative;
    width: 1200px;
    height: 1200px;
    font-family: "Cinzel", "Trajan Pro", serif;
  }
  .label {
    position: absolute;
    top: 411px;
    width: 279px;
    height: 500px;
    overflow: hidden;
  }
  .label--light {
    left: 149px;
    background: var(--label-light);
    color: var(--ink-dark);
    box-shadow: 0 0 6px var(--soft-shadow);
  }
  .label--dark {
    left: 755px;
    background: var(--label-dark);
    color: var(--ink-light);
  }
  .brand-dot {
    position: absolute;
    top: 56px;
    left: 124px;
    width: 46px;
    height: 46px;
    border-radius: 50%;
  }
  .label--light .brand-dot { background: var(--blossom-pink); }
  .label--dark .brand-dot { background: var(--ink-light); }
  .brand-name {
    position: absolute;
    top: 120px;
    left: 8px;
    width: 100%;
    text-align: center;
    font-size: 16px;
    font-weight: 400;
    letter-spacing: 3.6px;
    white-space: nowrap;
    text-transform: uppercase;
  }
  .leaf-mark {
    position: absolute;
    top: 206px;
    left: 96px;
    width: 78px;
    height: 44px;
    border-radius: 4px;
  }
  .label--light .leaf-mark {
    background: linear-gradient(90deg, var(--blossom-pink), var(--leaf-green));
  }
  .label--dark .leaf-mark {
    background: linear-gradient(90deg, #e6e6e6, #ffffff);
  }
  .product-name {
    position: absolute;
    top: 252px;
    left: 0;
    width: 100%;
    text-align: center;
    font-size: 22px;
    font-weight: 400;
    letter-spacing: 1.8px;
    white-space: nowrap;
    font-variant: small-caps;
  }
  .green-band {
    position: absolute;
    top: 279px;
    left: 0;
    width: 100%;
    height: 221px;
    background: var(--leaf-green);
    color: var(--ink-light);
  }
  .slogan {
    position: absolute;
    top: 4px;
    left: 0;
    width: 100%;
    text-align: center;
    font-size: 15.5px;
    letter-spacing: 1px;
    white-space: nowrap;
    font-variant: small-caps;
  }
  .vine-art {
    position: absolute;
    top: 32px;
    left: 0;
    width: 100%;
    height: 150px;
    background: linear-gradient(160deg, var(--leaf-green) 10%, var(--leaf-green-soft) 55%, var(--leaf-green) 95%);
  }
  .net-size {
    position: absolute;
    right: 29px;
    bottom: 11px;
    font-size: 11.5px;
    letter-spacing: 0.5px;
    white-space: nowrap;
  }
</style>
</head>
<body>
<main class="canvas">

  <section class="label label--light" aria-label="Pure Coconut Oil label, white version">
    <span class="brand-dot" aria-hidden="true"></span>
    <p class="brand-name">Maple Fern Gala</p>
    <div class="leaf-mark" role="img" aria-label="Two small leaves, one pink and one green"></div>
    <h1 class="product-name">Pure Coconut Oil</h1>
    <div class="green-band">
      <p class="slogan">Hydrate your skin and hair</p>
      <div class="vine-art" role="img" aria-label="White curling vine with leaves across the green band"></div>
      <p class="net-size">8 FL OZ 236ML</p>
    </div>
  </section>

  <section class="label label--dark" aria-label="Pure Coconut Oil label, black version">
    <span class="brand-dot" aria-hidden="true"></span>
    <p class="brand-name">Maple Fern Gala</p>
    <div class="leaf-mark" role="img" aria-label="Two small white leaves"></div>
    <h1 class="product-name">Pure Coconut Oil</h1>
    <div class="green-band">
      <p class="slogan">Hydrate your skin and hair</p>
      <div class="vine-art" role="img" aria-label="White curling vine with leaves across the green band"></div>
      <p class="net-size">8 FL OZ 236ML</p>
    </div>
  </section>

</main>
</body>
</html>
```